update company powerpoint deck - inject more power/personality into the deck

We would like a designer to provide us with a powerpoint template based on our brand guidelines. Current brand guidelines, colours and existing deck provided.
Current deck lacks punch. We really like our black and white elements - but need options for graphs, tables and charts. We potentially need more supplementary colours to what is currently in our brand guidelines.

Target Market(s)

listed companies - B2B. We are a management consulting company.

Industry/Entity Type

Consulting

Font styles to use
Serif
Sans Serif

Requirements
Must have
• Slides that are common for consulting companies.
The ability to use the deck as a report - not just a presentation format

```html
<!DOCTYPE html>
<html lang="en">
<head>
<meta charset="utf-8">
<title>Harlow Vantis – Presentation Template</title>
<link href="https://fonts.googleapis.com/css2?family=Lato:wght@300;400;700&display=swap" rel="stylesheet">
<style>
:root{
  --ink:#0b0b0b;
  --paper:#ffffff;
  --grey:#7a7a7a;
  --grey-light:#b9b9b9;
  --rule:#e4e4e4;
  --teal:#5fb3a6;
  --red:#c0272d;
  --blue:#3b63a8;
  --navy:#24427a;
  --slate:#555a60;
  --mint:#e6efec;
}
*{box-sizing:border-box;margin:0;padding:0}
html,body{width:900px;height:1200px;overflow:hidden;background:var(--paper)}
body{font-family:"Lato",Arial,sans-serif;color:var(--ink)}
.canvas{position:relative;width:900px;height:1200px;overflow:hidden;background:var(--paper)}
.brand-head{position:absolute;top:40px;left:0;width:900px;text-align:center;font-weight:400;font-size:14px;letter-spacing:10px;line-height:20px;padding-left:10px}

.slide{position:absolute;width:237px;height:133px;background:var(--paper);box-shadow:0 3px 9px rgba(0,0,0,.16);overflow:hidden}
.abs{position:absolute}
.block{position:absolute;background:var(--ink)}
.mark{position:absolute;top:9px;right:18px;font-size:3.4px;font-weight:700;letter-spacing:2.3px}
.mark.light{color:var(--paper)}
.foot{position:absolute;left:15px;right:15px;bottom:3px;display:flex;justify-content:space-between;font-size:1.9px;color:var(--grey-light)}
.title{position:absolute;font-weight:300;font-size:7px;letter-spacing:.2px;color:#222;text-transform:uppercase}
.title.center{left:0;right:0;text-align:center}
.subtitle{position:absolute;left:0;right:0;text-align:center;font-size:5px;font-weight:300;color:var(--teal)}
.para{position:absolute;font-size:2.3px;line-height:1.5;color:var(--grey);text-align:justify}
.para.white{color:#ddd}
.photo{position:absolute}
.tag{font-size:3px;font-weight:700;color:#222;text-transform:uppercase}

/* slide 1 */
.cover-photo{background:linear-gradient(160deg,#5f6b78 0%,#2c3540 45%,#11161c 100%)}
.brand-mini{position:absolute;color:var(--paper);font-size:4px;letter-spacing:3.4px;line-height:6px}
.cover-title{position:absolute;left:6px;top:64px;width:60px;color:var(--paper);text-align:center}
.cover-title b{display:block;font-size:3px;font-weight:700}
.cover-title span{display:block;font-size:2.3px;margin-top:2px}

/* agenda */
.agenda-word{position:absolute;left:0;top:26px;width:122px;height:81px;display:flex;align-items:center;justify-content:center;color:var(--paper);font-size:9.5px;font-weight:300}
.agenda-list{position:absolute;left:131px;top:27px;list-style:none}
.agenda-list li{display:flex;align-items:flex-start;height:11.6px}
.agenda-list .num{font-size:6.5px;font-weight:300;color:var(--grey);width:11px;line-height:7px}
.agenda-list .tag{font-size:3.1px;font-weight:400;line-height:3.6px}
.agenda-list .desc{display:block;font-size:2.3px;color:var(--grey);font-weight:400;text-transform:none}

.person{background:linear-gradient(180deg,#d5d7da,#9ea3a8)}
.sign{position:absolute;text-align:right;font-size:2.5px;color:var(--grey)}
.sign b{display:block;font-size:3.6px;font-weight:400;color:#333}

/* services numbered */
.svc-item{position:absolute;left:132px;width:90px;display:flex;gap:4px}
.svc-item .num{font-size:11px;font-weight:300;color:var(--teal);line-height:11px}
.svc-item .tag{font-size:2.6px;font-weight:400;margin-bottom:1px}
.svc-item .para{position:static;font-size:2.2px}

.icon-box{position:absolute;left:0;top:50px;width:65px;height:55px;background:var(--ink);display:flex;align-items:center;justify-content:center}
.bullets{position:absolute;left:82px;top:52px;width:148px;font-size:3.9px;line-height:4.9px;color:#222;padding-left:5px}
.bullets li{margin:0}

/* services grid */
.svc-cell{position:absolute;display:flex;align-items:center;gap:3px;width:55px}
.svc-cell .sq{width:16px;height:16px;background:var(--ink);flex:none;display:flex;align-items:center;justify-content:center}
.svc-cell span{font-size:2px;line-height:2.5px;color:var(--grey-light);text-transform:uppercase}

/* gallery */
.gallery-card{position:absolute;top:40px;width:47px}
.gallery-card .photo{position:static;height:46px}
.gallery-card .tag{font-size:2.4px;font-weight:400;text-align:center;margin:3px 0 1px}
.gallery-card .para{position:static;font-size:2.3px;text-align:justify}

/* stats ring */
.ring-label{position:absolute;top:82px;width:40px;text-align:center;font-size:2.4px;line-height:3px}
.ring-label b{display:block;font-weight:400}
.ring-label span{color:#8a8a8a}

/* deals */
.deal-card{position:absolute;top:55px;width:37px;height:37px;background:var(--paper);box-shadow:1px 1px 2px rgba(0,0,0,.2);display:flex;align-items:center;justify-content:center}
.deal-label{position:absolute;top:95px;width:37px;text-align:center;font-size:3.4px;line-height:4px;color:#333}

.stat{position:absolute;top:55px;width:46px;text-align:center}
.stat b{display:block;font-size:16px;font-weight:400;line-height:17px}
.stat span{display:block;font-size:2.2px;color:var(--teal);margin-top:1px}

.insight{position:absolute;width:52px}
.insight .head{display:flex;align-items:baseline;gap:3px;font-size:2.5px;color:var(--teal)}
.insight .head b{font-size:8px;font-weight:300}
.insight.right .head{justify-content:flex-end}
.insight.right .head span{color:var(--navy)}
.insight .para{position:static;margin-top:1px}
.insight.right .para{text-align:right}

.side-title{position:absolute;left:12px;top:33px;width:34px;color:var(--paper);font-size:4px;font-weight:300;line-height:4.8px}
.side-text{position:absolute;left:12px;top:45px;width:34px;color:#ddd;font-size:2.3px;line-height:3.1px;text-align:justify}
</style>
</head>
<body>
<div class="canvas">

  <div class="brand-head">HARLOW<br>VANTIS</div>

  <!-- 1 Cover -->
  <section class="slide" style="left:41px;top:112px">
    <div class="block" style="left:0;top:19px;width:71px;height:95px"></div>
    <div class="brand-mini" style="left:16px;top:26px">HARLOW<br>VANTIS</div>
    <div class="cover-title"><b>YOUR TITLE PRESENTATION HERE</b><span>Your sub title presentation goes here</span></div>
    <div class="photo cover-photo" role="img" aria-label="City skyline of glass towers at dusk" style="left:71px;top:19px;width:166px;height:95px"></div>
  </section>

  <!-- 2 Agenda -->
  <section class="slide" style="left:326px;top:112px">
    <div class="mark">HARLOW VANTIS</div>
    <div class="block" style="left:0;top:26px;width:122px;height:81px"></div>
    <div class="agenda-word">Agenda</div>
    <ol class="agenda-list">
      <li><span class="num">01</span><span class="tag">Opportunity<span class="desc">Investment Highlights</span></span></li>
      <li><span class="num">02</span><span class="tag">Property Overview<span class="desc">Property Description, Market Overview</span></span></li>
      <li><span class="num">03</span><span class="tag">Market Overview<span class="desc">Submarket Overview &amp; Comparables</span></span></li>
      <li><span class="num">04</span><span class="tag">Business Plan<span class="desc">Renovations, Timeline, Case Study</span></span></li>
      <li><span class="num">05</span><span class="tag">Investment Structure<span class="desc">Summary of Terms, Sample Investment</span></span></li>
      <li><span class="num">06</span><span class="tag">HV Partners Overview<span class="desc">Strategy, Timeline, Principals, Process</span></span></li>
      <li><span class="num">07</span><span class="tag">Appendix<span class="desc">Representative Transactions</span></span></li>
    </ol>
    <div class="foot"><span>www.harlowvantis.com</span><span>Harlow Vantis 2022 Confidential</span><span>Page | 2</span></div>
  </section>

  <!-- 3 Welcome -->
  <section class="slide" style="left:611px;top:112px">
    <div class="mark">HARLOW VANTIS</div>
    <div class="block" style="left:0;top:49px;width:90px;height:84px"></div>
    <div class="photo person" role="img" aria-label="Portrait of the chief executive" style="left:58px;top:23px;width:65px;height:64px"></div>
    <div class="title" style="left:131px;top:26px;font-size:7.5px;line-height:9px">Welcome<br>Message</div>
    <p class="para" style="left:131px;top:51px;width:87px">Our firm partners with boards and leadership teams to build trust with investors and shape lasting value. We combine market insight, clear advice and careful execution on every mandate. This deck outlines who we are, how we work and the results we deliver for listed companies across regions and sectors. We look forward to working together on the decisions that matter most to your shareholders.</p>
    <div class="sign" style="right:19px;top:110px"><span style="font-size:3px;color:#555">Dario Conti</span><br>CEO</div>
    <div class="foot"><span>www.harlowvantis.com</span><span>Harlow Vantis 2022 Confidential</span><span>Page | 3</span></div>
  </section>

  <!-- 4 Presenter -->
  <section class="slide" style="left:41px;top:293px">
    <div class="mark">HARLOW VANTIS</div>
    <div class="block" style="left:0;top:0;width:62px;height:133px"></div>
    <div class="photo person" role="img" aria-label="Portrait of the presenter" style="left:27px;top:29px;width:67px;height:75px"></div>
    <div class="title" style="left:111px;top:31px">Today Presenter</div>
    <p class="para" style="left:111px;top:43px;width:100px">Our presenter has advised boards and investors for over three decades, guiding companies through governance reviews, contested meetings and major transactions. His work spans markets in Europe, the Americas and Asia, with a focus on building long term trust between issuers and their shareholders and delivering clear, practical advice at every stage.</p>
    <div class="sign" style="left:160px;top:72px;width:40px;text-align:center">Best Regards</div>
    <div class="sign" style="left:160px;top:95px;width:40px;text-align:center"><b>Peter Hale</b>Chairman Emeritus</div>
    <div class="foot"><span>www.harlowvantis.com</span><span>Harlow Vantis 2022 Confidential</span><span>Page | 4</span></div>
  </section>

  <!-- 5 Regional leader -->
  <section class="slide" style="left:326px;top:293px">
    <div class="mark">HARLOW VANTIS</div>
    <div class="block" style="left:0;top:19px;width:78px;height:95px"></div>
    <div class="title" style="left:78px;width:159px;text-align:center;top:24px;font-size:6px;font-weight:400">Regional Leader</div>
    <div class="abs" style="left:78px;width:159px;text-align:center;top:32px;font-size:3px">Nathan Brooks CEO – APAC</div>
    <div class="photo" role="img" aria-label="Harbour waterfront landmark at sunset" style="left:51px;top:41px;width:111px;height:52px;background:linear-gradient(180deg,#c9a6c4 0%,#e9c3cc 45%,#aab3c8 75%,#6f7c8e 100%)"></div>
    <div class="photo person" role="img" aria-label="Portrait of the regional CEO" style="left:166px;top:41px;width:54px;height:52px"></div>
    <p class="para" style="left:81px;top:96px;width:139px">Our Asia Pacific team supports listed companies across the region with governance advice, investor engagement and transaction support. Led from our regional office, the team brings local knowledge and global reach to every client relationship, delivering clear counsel on the issues that shape shareholder value today and into the future.</p>
    <div class="foot"><span>www.harlowvantis.com</span><span>Harlow Vantis 2022 Confidential</span><span>Page | 5</span></div>
  </section>

  <!-- 6 Advisory services numbered -->
  <section class="slide" style="left:611px;top:293px">
    <div class="mark">HARLOW VANTIS</div>
    <div class="block" style="left:0;top:0;width:70px;height:125px"></div>
    <div class="title" style="left:85px;top:21px">Our Advisory Services</div>
    <div class="photo" role="img" aria-label="Glass office tower against a bright sky" style="left:16px;top:35px;width:106px;height:67px;background:linear-gradient(135deg,#cfe3f2 0%,#8fb3d2 45%,#3f6486 100%)"></div>
    <div class="svc-item" style="top:36px"><span class="num">01</span><div><div class="tag">Lorem ipsum dolor</div><p class="para">Governance reviews, board advice and investor outreach built around your annual meeting needs.</p></div></div>
    <div class="svc-item" style="top:60px"><span class="num">02</span><div><div class="tag">Lorem ipsum dolor</div><p class="para">Proxy solicitation and vote tracking that keeps your resolutions on course to pass.</p></div></div>
    <div class="svc-item" style="top:84px"><span class="num">03</span><div><div class="tag">Lorem ipsum dolor</div><p class="para">Activism defence and deal support for complex special situations and contests.</p></div></div>
    <div class="foot"><span>www.harlowvantis.com</span><span>Harlow Vantis 2022 Confidential</span><span>Page | 6</span></div>
  </section>

  <!-- 7 Retail services A -->
  <section class="slide" style="left:41px;top:475px">
    <div class="mark">HARLOW VANTIS</div>
    <div class="title center" style="top:21px;font-weight:400;font-size:6.5px">Our Advisory Services</div>
    <div class="subtitle" style="top:30px">Retail Services and Additional Capabilities</div>
    <div class="icon-box">
      <svg width="30" height="28" viewBox="0 0 30 28" fill="none" stroke="#fff" stroke-width="1.2">
        <circle cx="15" cy="5" r="3"/><path d="M9 17c0-4 3-7 6-7s6 3 6 7v8H9z"/>
        <circle cx="6" cy="10" r="2.3"/><path d="M1 26v-6c0-3 2-5 5-5"/>
        <circle cx="24" cy="10" r="2.3"/><path d="M29 26v-6c0-3-2-5-5-5"/>
        <circle cx="15" cy="19" r="2"/>
      </svg>
    </div>
    <ul class="bullets">
      <li>Strategic advice on corporate governance, board issues, compensation, sustainability and shareholder activism</li>
      <li>Ownership profile and analysis of shareholder expectations</li>
      <li>Comprehensive review and preparation for the annual meeting</li>
      <li>Vote projections and updates on shareholder voting policies</li>
      <li>Document review and recommendations</li>
      <li>Outreach and engagement with key investors and proxy advisory firms</li>
      <li>Presentations to the board and management on relevant trends in governance, sustainability, shareholder rights and activism</li>
    </ul>
    <div class="foot"><span>www.harlowvantis.com</span><span>Harlow Vantis 2022 Confidential</span><span>Page | 7</span></div>
  </section>

  <!-- 8 Retail services B -->
  <section class="slide" style="left:326px;top:475px">
    <div class="mark">HARLOW VANTIS</div>
    <div class="title center" style="top:21px;font-weight:400;font-size:6.5px">Our Advisory Services</div>
    <div class="subtitle" style="top:30px">Retail Services and Additional Capabilities</div>
    <div class="icon-box">
      <svg width="26" height="26" viewBox="0 0 26 26" fill="none" stroke="#fff" stroke-width="1.2">
        <circle cx="13" cy="10" r="6"/><path d="M6 10a7 7 0 0 1 14 0"/><rect x="4.5" y="9" width="2.5" height="4" rx="1"/><rect x="19" y="9" width="2.5" height="4" rx="1"/>
        <path d="M20 13c0 3-2 4-5 4"/><path d="M3 25c0-5 4-8 10-8s10 3 10 8z"/>
      </svg>
    </div>
    <ul class="bullets">
      <li>IPO Services</li>
      <li>Telephone solicitation campaigns</li>
      <li>Retail shareholder outreach programs</li>
      <li>Post-merger clean-up and asset reunification programs</li>
      <li>Odd-lot buyback situations</li>
      <li>Vote tabulation services</li>
      <li>Inspector of Election services</li>
      <li>Expert witness testimony services</li>
    </ul>
    <div class="foot"><span>www.harlowvantis.com</span><span>Harlow Vantis 2022 Confidential</span><span>Page | 8</span></div>
  </section>

  <!-- 9 Text + image -->
  <section class="slide" style="left:611px;top:475px">
    <div class="block" style="left:13px;top:14px;width:77px;height:119px"></div>
    <div class="brand-mini" style="left:37px;top:29px">HARLOW<br>VANTIS</div>
    <p class="para" style="left:107px;top:16px;width:111px">We help listed companies understand who owns their shares, what those investors expect and how to win their support. Our teams track voting trends, advise on governance and lead outreach programmes that build confidence ahead of every meeting. From routine annual meetings to contested votes, we give boards the facts and the plan they need to act with clarity and to protect long term value for all shareholders in every market we serve.</p>
    <div class="photo" role="img" aria-label="Colleagues reviewing documents at a desk" style="left:49px;top:62px;width:89px;height:57px;background:linear-gradient(135deg,#e8eef3 0%,#b9c8d6 55%,#7f93a6 100%)"></div>
    <p class="para" style="left:145px;top:70px;width:73px">Our approach starts with data and ends with action. We map the shareholder base, identify the votes that decide the outcome and design a campaign to reach them. Every step is tracked and reported so management always knows where support stands and what remains to be done before the record date and the final tally.</p>
    <div class="foot"><span></span><span>Harlow Vantis 2022 Confidential</span><span>Page | 10</span></div>
  </section>

  <!-- 10 Services grid -->
  <section class="slide" style="left:41px;top:656px">
    <div class="mark">HARLOW VANTIS</div>
    <div class="title center" style="top:22px">Our Advisory Services</div>
    <div class="svc-cell" style="left:10px;top:38px"><div class="sq"><svg width="10" height="10" viewBox="0 0 10 10" fill="none" stroke="#fff" stroke-width=".8"><circle cx="5" cy="3" r="1.5"/><path d="M2 9c0-2 1.3-3.5 3-3.5S8 7 8 9"/></svg></div><span>Corporate governance advisory services</span></div>
    <div class="svc-cell" style="left:68px;top:38px"><div class="sq"><svg width="10" height="10" viewBox="0 0 10 10" fill="none" stroke="#fff" stroke-width=".8"><path d="M5 1v8M2 3h6M2 3L1 6h2zM8 3L7 6h2zM3 9h4"/></svg></div><span>ESG advisory services</span></div>
    <div class="svc-cell" style="left:127px;top:38px"><div class="sq"><svg width="10" height="10" viewBox="0 0 10 10" fill="none" stroke="#fff" stroke-width=".8"><path d="M1 4h2l4-3v8L3 6H1zM3 6l1 3"/></svg></div><span>Proxy contests, hostile takeovers, shareholder activism and special situations</span></div>
    <div class="svc-cell" style="left:185px;top:38px"><div class="sq"><svg width="10" height="10" viewBox="0 0 10 10" fill="none" stroke="#fff" stroke-width=".8"><circle cx="5" cy="5" r="3.8"/><circle cx="5" cy="5" r="1.8"/></svg></div><span>Debt services</span></div>
    <div class="svc-cell" style="left:10px;top:66px"><div class="sq"><svg width="10" height="10" viewBox="0 0 10 10" fill="none" stroke="#fff" stroke-width=".8"><path d="M1 5l3 3 5-5-3-3z"/></svg></div><span>ESG survey services ESG monitoring</span></div>
    <div class="svc-cell" style="left:68px;top:66px"><div class="sq"><svg width="10" height="10" viewBox="0 0 10 10" fill="none" stroke="#fff" stroke-width=".8"><circle cx="5" cy="5" r="4"/><path d="M1 5h8M5 1c-2 2.5-2 5.5 0 8M5 1c2 2.5 2 5.5 0 8"/></svg></div><span>Capital market intelligence services</span></div>
    <div class="svc-cell" style="left:127px;top:66px"><div class="sq"><svg width="10" height="10" viewBox="0 0 10 10" fill="none" stroke="#fff" stroke-width=".8"><rect x="1" y="2" width="8" height="6"/><path d="M3 5l1.5 1.5L7 4"/></svg></div><span>Proxy solicitation and shareholder meeting services</span></div>
    <div class="svc-cell" style="left:185px;top:66px"><div class="sq"><svg width="10" height="10" viewBox="0 0 10 10" fill="none" stroke="#fff" stroke-width=".8"><rect x="1.5" y="1" width="2.5" height="8"/><rect x="6" y="3" width="2.5" height="6"/></svg></div><span>SPAC advisory services</span></div>
    <div class="svc-cell" style="left:40px;top:93px"><div class="sq"><svg width="10" height="10" viewBox="0 0 10 10" fill="none" stroke="#fff" stroke-width=".8"><circle cx="5" cy="4" r="2.5"/><path d="M1 10c0-2.5 2-4 4-4s4 1.5 4 4"/></svg></div><span>Retail services and additional capabilities</span></div>
    <div class="svc-cell" style="left:99px;top:93px"><div class="sq"><svg width="10" height="10" viewBox="0 0 10 10" fill="none" stroke="#fff" stroke-width=".8"><rect x="1" y="1" width="8" height="8"/><path d="M1 4h8M1 7h8M4 1v8M7 1v8"/></svg></div><span>Board of director services</span></div>
    <div class="svc-cell" style="left:157px;top:93px;width:70px"><div class="sq"><svg width="10" height="10" viewBox="0 0 10 10" fill="none" stroke="#fff" stroke-width=".8"><rect x="1" y="2.5" width="8" height="5"/><circle cx="5" cy="5" r="1.3"/></svg></div><span>Services for registered funds – mutual funds, exchange traded funds and closed-end funds</span></div>
    <div class="foot"><span>www.harlowvantis.com</span><span>Harlow Vantis 2022 Confidential</span><span>Page | 9</span></div>
  </section>

  <!-- 11 Gallery -->
  <section class="slide" style="left:326px;top:656px">
    <div class="mark">HARLOW VANTIS</div>
    <div class="title center" style="top:23px">Projects Gallery</div>
    <div class="gallery-card" style="left:17px"><div class="photo" role="img" aria-label="Glass office tower" style="background:linear-gradient(135deg,#d9e8f3,#6f8fab)"></div><div class="tag">Lorem ipsum dolor</div><p class="para">Proxy campaign for a listed industrial group with record turnout.</p></div>
    <div class="gallery-card" style="left:68px"><div class="photo" role="img" aria-label="City towers at night" style="background:linear-gradient(160deg,#55606c,#1c2229)"></div><div class="tag">Lorem ipsum dolor</div><p class="para">Activism defence for a regional bank across three markets.</p></div>
    <div class="gallery-card" style="left:118px"><div class="photo" role="img" aria-label="Business meeting with documents" style="background:linear-gradient(135deg,#eef2f5,#a8b6c3)"></div><div class="tag">Lorem ipsum dolor</div><p class="para">Governance review for a newly listed technology company.</p></div>
    <div class="block" style="left:169px;top:41px;width:68px;height:70px"></div>
    <p class="para white" style="left:174px;top:45px;width:58px">Each project brings together research, strategy and outreach. We work alongside management from the first briefing to the final vote, adjusting the plan as results arrive. Our teams report daily on progress and flag risks early so that the board can respond quickly. The outcome is a clear path to support and a stronger relationship with investors long after the meeting has closed and the results are filed.</p>
    <div class="foot"><span>www.harlowvantis.com</span><span>Harlow Vantis 2022 Confidential</span><span>Page | 11</span></div>
  </section>

  <!-- 12 Rings -->
  <section class="slide" style="left:611px;top:656px">
    <div class="mark">HARLOW VANTIS</div>
    <div class="block" style="left:0;top:27px;width:237px;height:80px"></div>
    <svg class="abs" style="left:0;top:27px" width="237" height="80" viewBox="0 0 237 80" fill="none" stroke-width="1.4" font-family="Lato, Arial, sans-serif" font-weight="300" font-size="11" text-anchor="middle">
      <g transform="rotate(-90 38 31)"><circle cx="38" cy="31" r="20" stroke="var(--teal)" stroke-dasharray="99.3 125.7"/></g>
      <text x="38" y="35" fill="var(--teal)" stroke="none">79%</text>
      <g transform="rotate(-90 92 31)"><circle cx="92" cy="31" r="20" stroke="var(--red)" stroke-dasharray="121.9 125.7"/></g>
      <text x="92" y="35" fill="var(--red)" stroke="none">97%</text>
      <g transform="rotate(-90 145 31)"><circle cx="145" cy="31" r="20" stroke="var(--blue)" stroke-dasharray="66.6 125.7"/></g>
      <text x="145" y="35" fill="var(--blue)" stroke="none">53%</text>
      <g transform="rotate(-90 198 31)"><circle cx="198" cy="31" r="20" stroke="#6a6a6a" stroke-dasharray="89.2 125.7"/></g>
      <text x="198" y="35" fill="#8a8a8a" stroke="none">71%</text>
    </svg>
    <div class="ring-label" style="left:18px"><b style="color:var(--teal)">LOREM IPSUM DOLOR</b><span>Share of votes cast in favour at meetings we supported</span></div>
    <div class="ring-label" style="left:72px"><b style="color:var(--red)">LOREM IPSUM DOLOR</b><span>Share of contested situations resolved for our clients</span></div>
    <div class="ring-label" style="left:125px"><b style="color:var(--blue)">LOREM IPSUM DOLOR</b><span>Share of mandates that are repeat client engagements</span></div>
    <div class="ring-label" style="left:178px"><b style="color:#8a8a8a">LOREM IPSUM DOLOR</b><span>Average retail turnout across managed campaigns</span></div>
    <div class="foot"><span>www.harlowvantis.com</span><span>Harlow Vantis 2022 Confidential</span><span>Page | 12</span></div>
  </section>

  <!-- 13 Latest deals -->
  <section class="slide" style="left:41px;top:838px">
    <div class="mark">HARLOW VANTIS</div>
    <div class="block" style="left:0;top:26px;width:46px;height:107px"></div>
    <div class="title" style="left:46px;right:0;text-align:center;top:38px;font-weight:400">Our Latest Deals</div>
    <div class="deal-card" style="left:52px"><svg width="24" height="20" viewBox="0 0 24 20" fill="none" stroke="var(--teal)" stroke-width=".9"><path d="M1 8l6-6 5 4 5-4 6 6-10 10z"/><path d="M7 9l4 4M10 7l4 4M13 6l3 3"/></svg></div>
    <div class="deal-card" style="left:97px"><svg width="24" height="16" viewBox="0 0 24 16" fill="none" stroke="var(--teal)" stroke-width=".9"><rect x="1" y="1" width="22" height="14"/><circle cx="12" cy="8" r="3.5"/><path d="M4 5h4M4 11h4M16 5h4M16 11h4"/></svg></div>
    <div class="deal-card" style="left:142px"><svg width="24" height="24" viewBox="0 0 24 24" fill="none" stroke="var(--teal)" stroke-width=".9"><rect x="2" y="6" width="6" height="17"/><rect x="16" y="2" width="6" height="21"/><path d="M9 11h6l-2-2M15 15H9l2 2M4 9v2M4 14v2M18 6v2M18 11v2M18 16v2"/></svg></div>
    <div class="deal-card" style="left:186px"><svg width="24" height="22" viewBox="0 0 24 22" fill="none" stroke="var(--teal)" stroke-width=".9"><path d="M2 9l14-7v18L2 13z"/><path d="M5 13l2 7h3l-1-6"/><path d="M19 8h4M18 4l3-2M18 13l3 2"/></svg></div>
    <div class="deal-label" style="left:52px">M&amp;A Deals</div>
    <div class="deal-label" style="left:97px">Debt Deals</div>
    <div class="deal-label" style="left:142px">Spac Deals</div>
    <div class="deal-label" style="left:186px">Activism<br>Advisory</div>
    <div class="foot"><span></span><span>Harlow Vantis 2022 Confidential</span><span>Page | 13</span></div>
  </section>

  <!-- 14 Numbers -->
  <section class="slide" style="left:326px;top:838px">
    <div class="mark">HARLOW VANTIS</div>
    <div class="title center" style="top:28px;font-weight:300">Our Advisory Services</div>
    <div class="stat" style="left:20px"><b>267</b><span>LOREM IPSUM DOLOR</span></div>
    <div class="stat" style="left:70px"><b>1023</b><span>LOREM IPSUM DOLOR</span></div>
    <div class="stat" style="left:122px"><b>34</b><span>LOREM IPSUM DOLOR</span></div>
    <div class="stat" style="left:166px"><b>121</b><span>LOREM IPSUM DOLOR</span></div>
    <div class="foot"><span></span><span>Harlow Vantis 2022 Confidential</span><span>Page | 14</span></div>
  </section>

  <!-- 15 Company insights -->
  <section class="slide" style="left:611px;top:838px">
    <div class="mark">HARLOW VANTIS</div>
    <div class="title center" style="top:19px;font-weight:400">Company Insights</div>
    <div class="subtitle" style="top:28px;font-size:2.8px">Four pillars that shape how we advise every client and market</div>
    <svg class="abs" style="left:0;top:0" width="237" height="133" viewBox="0 0 237 133" fill="none">
      <circle cx="92" cy="52" r="10.5" fill="var(--teal)"/>
      <circle cx="143" cy="52" r="10.5" fill="var(--navy)"/>
      <circle cx="92" cy="102" r="10.5" fill="var(--blue)"/>
      <circle cx="143" cy="102" r="10.5" fill="var(--slate)"/>
      <circle cx="117.5" cy="77" r="15" fill="var(--ink)"/>
      <g stroke="#fff" stroke-width=".7">
        <rect x="87" y="47" width="10" height="10"/><path d="M87 52h10M92 47v10"/>
        <circle cx="143" cy="52" r="4.5"/><path d="M138.5 52h9M143 47.5c-2 3-2 6 0 9M143 47.5c2 3 2 6 0 9"/>
        <path d="M92 97v10M88 99h8M88 99l-1.5 3h3zM96 99l-1.5 3h3z"/>
        <path d="M138 102l3-3 2 2 2-2 3 3-5 5z"/>
      </g>
      <text x="117.5" y="76" fill="#fff" font-family="Lato, Arial, sans-serif" font-size="2.6" letter-spacing="1.6" text-anchor="middle">HARLOW</text>
      <text x="117.5" y="80.5" fill="#fff" font-family="Lato, Arial, sans-serif" font-size="2.6" letter-spacing="1.6" text-anchor="middle">VANTIS</text>
    </svg>
    <div class="insight" style="left:19px;top:42px"><div class="head"><b>1</b>LOREM IPSUM DOLOR</div><p class="para">Deep knowledge of the shareholder base and how each group tends to vote on key items.</p></div>
    <div class="insight" style="left:19px;top:89px"><div class="head"><b>2</b>LOREM IPSUM DOLOR</div><p class="para">Clear governance advice shaped by current policy and investor expectations worldwide.</p></div>
    <div class="insight right" style="left:165px;top:42px"><div class="head"><span>LOREM IPSUM DOLOR</span><b style="color:var(--navy)">3</b></div><p class="para">Global reach with local teams who know each market and its rules in detail.</p></div>
    <div class="insight right" style="left:165px;top:89px"><div class="head"><span style="color:var(--slate)">LOREM IPSUM DOLOR</span><b style="color:var(--slate)">4</b></div><p class="para">Long term partnerships built on trust, results and honest advice at every stage.</p></div>
    <div class="foot"><span>www.harlowvantis.com</span><span>Harlow Vantis 2022 Confidential</span><span>Page | 15</span></div>
  </section>

  <!-- 16 Strategic roadmap table -->
  <section class="slide" style="left:41px;top:1020px">
    <div class="mark">HARLOW VANTIS</div>
    <div class="block" style="left:0;top:29px;width:54px;height:82px"></div>
    <div class="side-title">STRATEGIC<br>ROADMAP</div>
    <p class="side-text">A one page view of purpose, values and the shifts needed to reach our goals by year two and year three of the plan.</p>
    <svg class="abs" style="left:56px;top:28px" width="170" height="84" viewBox="0 0 170 84" font-family="Lato, Arial, sans-serif" fill="none">
      <g font-size="2.2" font-weight="700" fill="#222">
        <text x="3" y="7">MISSION</text><text x="3" y="20">VALUES</text>
        <text x="2" y="31">INGREDIENT</text><text x="5" y="34.5">S FOR</text><text x="4" y="38">CHANGE</text>
        <text x="2" y="56">BY YEAR 2</text><text x="2" y="78">BY YEAR 3</text>
      </g>
      <rect x="27.5" y=".5" width="138" height="83" stroke="var(--red)" stroke-width=".7" fill="#fff"/>
      <rect x="30" y="3" width="133" height="6" fill="#f1f1f1"/>
      <text x="96" y="6.8" font-size="1.8" fill="#555" text-anchor="middle">To connect, support and inform efforts to improve the health of communities in our region</text>
      <g fill="#f1f1f1">
        <rect x="30" y="12" width="25" height="11"/><rect x="57" y="12" width="25" height="11"/><rect x="84" y="12" width="25" height="11"/><rect x="111" y="12" width="25" height="11"/><rect x="138" y="12" width="25" height="11"/>
        <rect x="30" y="26" width="31" height="10"/><rect x="63" y="26" width="31" height="10"/><rect x="96" y="26" width="33" height="10"/><rect x="131" y="26" width="32" height="10"/>
        <rect x="30" y="39" width="133" height="5"/>
        <rect x="30" y="47" width="133" height="24" fill="#eef4f2"/>
        <rect x="30" y="74" width="133" height="7"/>
      </g>
      <g font-size="1.8" font-weight="700" fill="#333" text-anchor="middle">
        <text x="42.5" y="15">EMPATHY</text><text x="69.5" y="15">EQUITY</text><text x="96.5" y="15">INTEGRITY</text><text x="123.5" y="15">OPENNESS</text><text x="150.5" y="15">KNOWLEDGE</text>
      </g>
      <g font-size="1.6" fill="#777" text-anchor="middle">
        <text x="42.5" y="19">Feeling from others</text><text x="69.5" y="19">Fair for everyone</text><text x="96.5" y="19">Honest and open</text><text x="123.5" y="19">Always learning</text><text x="150.5" y="19">Shared wisdom</text>
        <text x="45.5" y="31.5">Policy and system change</text><text x="78.5" y="31.5">Multi-sector partners</text><text x="112.5" y="31.5">Paradigm shift</text><text x="147" y="31.5">Build trust and equity</text>
        <text x="96" y="42.3">Company will identify and build relationships with stakeholders to drive progress</text>
        <text x="96" y="78.3">Company will support stakeholders in building networks of champions</text>
      </g>
      <g fill="#fff" stroke="#d8e4e0" stroke-width=".3">
        <rect x="32" y="49" width="23" height="20"/><rect x="58" y="49" width="23" height="20"/><rect x="84" y="49" width="23" height="20"/><rect x="110" y="49" width="23" height="20"/><rect x="136" y="49" width="25" height="20"/>
      </g>
      <g font-size="1.8" font-weight="700" fill="#333" text-anchor="middle">
        <text x="43.5" y="52">RESISTANT</text><text x="69.5" y="52">CURIOUS</text><text x="95.5" y="52">AWARE</text><text x="121.5" y="52">ADVOCATE</text><text x="148.5" y="52">CHAMPION</text>
      </g>
      <g stroke="#bbb" stroke-width=".4">
        <path d="M34 55h18M34 58h16M34 61h18M60 55h18M60 58h16M60 61h18M86 55h18M86 58h16M86 61h18M112 55h18M112 58h16M112 61h18M138 55h20M138 58h16M138 61h18"/>
      </g>
    </svg>
    <div class="foot"><span>www.harlowvantis.com</span><span>Harlow Vantis 2022 Confidential</span><span>Page | 16</span></div>
  </section>

  <!-- 17 Strategy map -->
  <section class="slide" style="left:326px;top:1020px">
    <div class="mark">HARLOW VANTIS</div>
    <div class="block" style="left:0;top:29px;width:54px;height:82px"></div>
    <div class="side-title">STRATEGIC<br>ROADMAP</div>
    <p class="side-text">A balanced view of how learning and internal work drive customer value and long term financial results for shareholders.</p>
    <svg class="abs" style="left:56px;top:30px" width="172" height="82" viewBox="0 0 172 82" font-family="Lato, Arial, sans-serif" fill="none">
      <rect x="0" y="0" width="172" height="82" rx="4" fill="var(--mint)"/>
      <rect x="0" y="25" width="172" height="37" fill="#dde3e4"/>
      <g font-size="2.3" font-weight="700" fill="#222" text-anchor="middle">
        <text x="12" y="17">FINANCIAL</text><text x="12" y="36">CUSTOMER</text><text x="12" y="55">INTERNAL</text><text x="12" y="73">LEARNING</text><text x="12" y="76">&amp; GROWTH</text>
      </g>
      <g stroke="#555" stroke-width=".5">
        <rect x="8" y="8" width="7" height="5"/><circle cx="12" cy="29" r="1.6"/><path d="M9 33c0-2 1.3-2.5 3-2.5s3 .5 3 2.5"/><rect x="8" y="47" width="7" height="4" rx="1"/><path d="M9 69l2-2 2 1 2-3"/>
      </g>
      <rect x="84" y="3" width="32" height="6" rx="3" fill="var(--teal)"/>
      <text x="100" y="6.8" font-size="1.8" fill="#fff" text-anchor="middle">Long-term Shareholder Value</text>
      <g fill="var(--teal)">
        <rect x="26" y="12" width="34" height="5" rx="2.5"/><rect x="62" y="12" width="34" height="5" rx="2.5"/><rect x="98" y="12" width="34" height="5" rx="2.5"/><rect x="134" y="12" width="34" height="5" rx="2.5"/>
      </g>
      <g font-size="1.7" fill="#fff" text-anchor="middle">
        <text x="43" y="15.3">Improve cost structure</text><text x="79" y="15.3">Increase asset utilisation</text><text x="115" y="15.3">Expand revenue options</text><text x="151" y="15.3">Enhance customer value</text>
      </g>
      <text x="100" y="24" font-size="1.9" font-weight="700" fill="#222" text-anchor="middle">CUSTOMER VALUE PROPOSITION</text>
      <g fill="var(--navy)">
        <rect x="28" y="27" width="16" height="4" rx="2"/><rect x="47" y="27" width="16" height="4" rx="2"/><rect x="66" y="27" width="16" height="4" rx="2"/><rect x="85" y="27" width="16" height="4" rx="2"/><rect x="104" y="27" width="16" height="4" rx="2"/><rect x="123" y="27" width="16" height="4" rx="2"/><rect x="142" y="27" width="16" height="4" rx="2"/>
      </g>
      <g font-size="1.7" fill="#fff" text-anchor="middle">
        <text x="36" y="29.7">Price</text><text x="55" y="29.7">Quality</text><text x="74" y="29.7">Availability</text><text x="93" y="29.7">Selection</text><text x="112" y="29.7">Function</text><text x="131" y="29.7">Service</text><text x="150" y="29.7">Brand</text>
      </g>
      <g font-size="1.7" fill="#444" text-anchor="middle"><text x="55" y="34">Product/Service Activity</text><text x="131" y="34">Relationship</text><text x="150" y="34">Image</text></g>
      <g fill="#fff"><rect x="28" y="38" width="30" height="20"/><rect x="62" y="38" width="30" height="20"/><rect x="96" y="38" width="30" height="20"/><rect x="130" y="38" width="30" height="20"/></g>
      <g fill="var(--slate)"><rect x="28" y="38" width="30" height="4"/><rect x="62" y="38" width="30" height="4"/><rect x="96" y="38" width="30" height="4"/><rect x="130" y="38" width="30" height="4"/></g>
      <g font-size="1.6" fill="#fff" text-anchor="middle"><text x="43" y="40.6">Operations Processes</text><text x="77" y="40.6">Customer Processes</text><text x="111" y="40.6">Innovation Processes</text><text x="145" y="40.6">Regulatory Processes</text></g>
      <g font-size="1.6" fill="#555" text-anchor="middle">
        <text x="43" y="46">Supply, Production</text><text x="43" y="49">Distribution, Risk</text><text x="77" y="46">Selection, Acquisition</text><text x="77" y="49">Retention, Growth</text><text x="111" y="46">Opportunity ID, R&amp;D</text><text x="111" y="49">Design, Launch</text><text x="145" y="46">Environment, Safety</text><text x="145" y="49">Employment, Community</text>
      </g>
      <g fill="var(--red)"><rect x="28" y="64" width="30" height="14" rx="1"/><rect x="62" y="64" width="30" height="14" rx="1"/><rect x="96" y="64" width="30" height="14" rx="1"/><rect x="130" y="64" width="30" height="14" rx="1"/></g>
      <g font-size="1.6" fill="#fff" text-anchor="middle">
        <text x="43" y="70">Active participation</text><text x="43" y="73">among everyone</text>
        <text x="77" y="69">Quality focused</text><text x="77" y="72">coworkers and</text><text x="77" y="75">attractive workplace</text>
        <text x="111" y="69">High competence</text><text x="111" y="72">and correct</text><text x="111" y="75">landscape analysis</text>
        <text x="145" y="69">High availability</text><text x="145" y="72">of information and</text><text x="145" y="75">efficient IT support</text>
      </g>
    </svg>
    <div class="foot"><span>www.harlowvantis.com</span><span>Harlow Vantis 2022 Confidential</span><span>Page | 17</span></div>
  </section>

  <!-- 18 7S model -->
  <section class="slide" style="left:611px;top:1020px">
    <div class="mark">HARLOW VANTIS</div>
    <div class="block" style="left:0;top:29px;width:54px;height:82px"></div>
    <div class="side-title">KESTREL 7S<br>MODEL</div>
    <p class="side-text">Seven linked elements that must stay aligned for a strategy to succeed, with shared value at the centre of the model.</p>
    <svg class="abs" style="left:56px;top:20px" width="181" height="105" viewBox="0 0 181 105" font-family="Lato, Arial, sans-serif" fill="none">
      <path d="M82 28h28l14 24-14 24H82L68 52z" stroke="#cfd3d6" stroke-width="5"/>
      <path d="M86 36h20l10 16-10 16H86L76 52z" fill="#fff" stroke="#b0b5b9" stroke-width=".6"/>
      <text x="96" y="50" font-size="2.5" font-weight="700" fill="#222" text-anchor="middle">SHARED VALUE</text>
      <text x="96" y="54" font-size="1.6" fill="#888" text-anchor="middle">What do we believe in</text>
      <circle cx="82" cy="28" r="8.5" fill="var(--slate)"/>
      <circle cx="110" cy="28" r="8.5" fill="#8ec3e6"/>
      <circle cx="124" cy="52" r="8.5" fill="var(--teal)"/>
      <circle cx="110" cy="76" r="8.5" fill="var(--blue)"/>
      <circle cx="82" cy="76" r="8.5" fill="#3f8f86"/>
      <circle cx="68" cy="52" r="8.5" fill="var(--navy)"/>
      <g font-size="1.9" font-weight="700" fill="#fff" text-anchor="middle">
        <text x="82" y="28.7">STRATEGY</text><text x="110" y="28.7">STRUCTURE</text><text x="124" y="52.7">SYSTEMS</text><text x="110" y="76.7">STYLE</text><text x="82" y="76.7">STAFF</text><text x="68" y="52.7">SKILLS</text>
      </g>
      <g font-size="1.6" fill="#777">
        <text x="20" y="22">What structure do we need</text><text x="20" y="24.5">to reach our stated goal?</text>
        <text x="133" y="22">What structure drives our</text><text x="133" y="24.5">ability to deliver the plan?</text>
        <text x="10" y="49">Which skills will help us</text><text x="10" y="51.5">deliver on the strategy?</text>
        <text x="145" y="49">What processes do we need</text><text x="145" y="51.5">to support each decision?</text>
        <text x="20" y="84">How should we manage</text><text x="20" y="86.5">and grow our people?</text>
        <text x="133" y="84">Which leadership style fits</text><text x="133" y="86.5">our strategic direction?</text>
      </g>
    </svg>
    <div class="foot"><span>www.harlowvantis.com</span><span>Harlow Vantis 2022 Confidential</span><span>Page | 18</span></div>
  </section>

</div>
</body>
</html>
```